Business Card Design

we specialise in supply of custom uniforms - teamwear to Schools and sporting clubs, see our website: www.kestrelkitworks.com.au, our main corporate colour is black and white, with small amount of gold/yellow

Industry/Entity Type

Business

Contact Information for Business Card

Kestrel Kit Works
Rowan Petrakis
Ph 03 6219 8805
Mobile 0418 262 740
email: rowan@kestrelkitworks.com.au
www.kestrelkitworks.com.au
like us on facebook

Requirements
Must have
• modern look & feel

```html
<!DOCTYPE html>
<html lang="en">
<head>
<meta charset="utf-8">
<title>Kestrel Kit Works – Business Card</title>
<link rel="stylesheet" href="https://fonts.googleapis.com/css2?family=Roboto+Condensed:wght@400;700&display=swap">
<style>
  :root {
    --page: #e9e6e1;
    --card-black: #0d0d0d;
    --swoosh-grey: #6f6f6f;
    --swoosh-light: #a4a4a4;
    --brand-yellow: #ffdd00;
    --text-white: #ffffff;
    --text-black: #111111;
  }
  * { box-sizing: border-box; margin: 0; padding: 0; }
  html, body {
    width: 1200px; height: 1023px; overflow: hidden;
    background: var(--page);
    font-family: "Roboto Condensed", "Arial Narrow", sans-serif;
  }
  .business-card {
    position: absolute; left: 150px; top: 254px;
    width: 900px; height: 514px;
    background: var(--card-black);
    overflow: hidden;
    box-shadow: 0 10px 30px rgba(0,0,0,0.25);
  }
  .card-shapes { position: absolute; inset: 0; }
  .brand {
    position: absolute; left: 60px; top: 70px;
    display: flex; align-items: center; gap: 14px;
  }
  .brand-square { width: 26px; height: 26px; background: var(--text-white); }
  .brand-name {
    color: var(--text-white); font-weight: 700; font-size: 40px;
    letter-spacing: 0.5px;
  }
  .contact-list {
    position: absolute; left: 60px; top: 200px;
    list-style: none; color: var(--text-white);
    font-size: 23px; line-height: 1;
  }
  .contact-list li { display: flex; align-items: center; gap: 16px; height: 40px; }
  .contact-icon { width: 22px; height: 22px; flex: none; }
  .social-squares {
    position: absolute; right: 38px; top: 26px; display: flex; gap: 10px;
  }
  .social-square { width: 30px; height: 30px; background: var(--brand-yellow); }
  .person {
    position: absolute; right: 70px; top: 180px; text-align: center;
    color: var(--text-black);
  }
  .person-name { font-weight: 700; font-size: 38px; letter-spacing: 0.5px; }
  .person-title { font-size: 20px; margin-top: 6px; }
</style>
</head>
<body>
  <div class="business-card">
    <svg class="card-shapes" width="900" height="514" viewBox="0 0 900 514">
      <path class="swoosh-grey" d="M520,0 C450,150 440,330 230,514 L300,514 C480,340 500,160 575,0 Z" fill="var(--swoosh-grey)"/>
      <path class="swoosh-light" d="M555,0 C485,160 480,340 300,514 L318,514 C500,345 515,165 590,0 Z" fill="var(--swoosh-light)"/>
      <path class="yellow-field" d="M640,0 C560,150 560,340 370,514 L900,514 L900,0 Z" fill="var(--brand-yellow)"/>
    </svg>

    <div class="social-squares" aria-label="Social links">
      <span class="social-square"></span>
      <span class="social-square"></span>
    </div>

    <div class="brand">
      <span class="brand-square"></span>
      <span class="brand-name">Kestrel Kit Works</span>
    </div>

    <ul class="contact-list">
      <li>
        <svg class="contact-icon" viewBox="0 0 22 22"><rect width="22" height="22" fill="var(--brand-yellow)"/><path d="M5 6 Q5 4 7 4 L15 4 Q17 4 17 6 L17 8 L14 8 L14 6 L8 6 L8 8 L5 8 Z M6 10 L16 10 L17 18 L5 18 Z" fill="var(--card-black)"/></svg>
        <span>03 6219 8805</span>
      </li>
      <li>
        <svg class="contact-icon" viewBox="0 0 22 22"><rect width="22" height="22" fill="var(--brand-yellow)"/><rect x="7" y="3" width="8" height="16" rx="1.5" fill="var(--card-black)"/><rect x="8.5" y="5" width="5" height="9" fill="var(--brand-yellow)"/></svg>
        <span>0418 262 740</span>
      </li>
      <li>
        <svg class="contact-icon" viewBox="0 0 22 22"><rect width="22" height="22" fill="var(--brand-yellow)"/><rect x="3" y="6" width="16" height="11" fill="var(--card-black)"/><path d="M3 6 L11 13 L19 6" stroke="var(--brand-yellow)" stroke-width="1.5" fill="none"/></svg>
        <span>rowan@kestrelkitworks.com.au</span>
      </li>
      <li>
        <svg class="contact-icon" viewBox="0 0 22 22"><circle cx="11" cy="11" r="10" fill="var(--brand-yellow)"/><path d="M1 11 H21 M11 1 V21 M4 5 Q11 8 18 5 M4 17 Q11 14 18 17" stroke="var(--card-black)" stroke-width="1.2" fill="none"/></svg>
        <span>www.kestrelkitworks.com.au</span>
      </li>
    </ul>

    <div class="person">
      <p class="person-name">Rowan Petrakis</p>
      <p class="person-title">Owner | Proprietor</p>
    </div>
  </div>
</body>
</html>
```